contemporary upscale hair salon

we need a business card design for a modern upscale salon. I would like the card to be vertical, simple, and easy to read. I would like a black matte finish on the info side with white on the back of the card, white lettering with a splash of red incorporated somewhere in there. I also want to incorporate embossing and/or cut out in the letters. The info I would like; Name of the business (Vessa Salon) stylist name (Joan) phone number(5093146620) and web address (www.vessasalon-example.com) I am open to putting shears on the card but without it looking too cheap. Looking for something really modern and edgy. these are just ideas I have, but feel free to show me your creative ideas.
please note: the website is still under construction please do not use any images or colors off the web page. Also i currently do not have a logo, that will be a future project.

```html
<!DOCTYPE html>
<html lang="en">
<head>
<meta charset="utf-8">
<title>Vessa Salon – Business Card</title>
<link rel="stylesheet" href="https://fonts.googleapis.com/css2?family=Jost:wght@400&display=swap">
<style>
  :root {
    --backdrop: #efefef;
    --card-white: #ffffff;
    --card-edge: #8a8a8a;
    --charcoal-light: #3c4348;
    --charcoal-dark: #262b2f;
    --salon-red: #d9261c;
    --ink-white: #ffffff;
  }
  html, body {
    margin: 0;
    padding: 0;
    width: 1200px;
    height: 892px;
    overflow: hidden;
    background: var(--backdrop);
  }
  .canvas {
    position: relative;
    width: 1200px;
    height: 892px;
    font-family: "Jost", "Futura", sans-serif;
  }
  .card {
    position: absolute;
    top: 91px;
    width: 414px;
    height: 708px;
    box-sizing: border-box;
  }
  .card--back {
    left: 174px;
    background: var(--card-white);
    border: 1px solid var(--card-edge);
  }
  .card--front {
    left: 611px;
    overflow: hidden;
  }
  .card__finish {
    position: absolute;
    inset: 0;
    background: linear-gradient(180deg, var(--charcoal-light) 0%, var(--charcoal-dark) 100%);
  }
  .wordmark {
    position: absolute;
    left: 0;
    right: 0;
    margin: 0;
    text-align: center;
    color: var(--salon-red);
    font-weight: 400;
    font-size: 40px;
    letter-spacing: 0.12em;
    text-transform: uppercase;
    line-height: 1;
  }
  .card--back .wordmark { top: 331px; }
  .card--front .wordmark { top: 184px; }
  .name-band {
    position: absolute;
    left: 0;
    right: 0;
    top: 430px;
    height: 51px;
    background: var(--salon-red);
    color: var(--ink-white);
    display: flex;
    align-items: center;
    justify-content: center;
    font-size: 22px;
    letter-spacing: 0.08em;
    text-transform: uppercase;
  }
  .contact {
    position: absolute;
    left: 0;
    right: 0;
    top: 550px;
    margin: 0;
    padding: 0;
    list-style: none;
    text-align: center;
    color: var(--ink-white);
    font-size: 19px;
    letter-spacing: 0.04em;
  }
  .contact__phone { margin-bottom: 38px; }
  .contact__web { margin-bottom: 8px; }
  .contact__social {
    display: inline-flex;
    align-items: center;
    gap: 6px;
  }
  .contact__social svg { display: block; }
</style>
</head>
<body>
<main class="canvas">
  <section class="card card--back" aria-label="Card back">
    <p class="wordmark">Vessa Salon</p>
  </section>

  <section class="card card--front" aria-label="Card front">
    <div class="card__finish" role="img" aria-label="Dark charcoal brushed-grain texture"></div>
    <p class="wordmark">Vessa Salon</p>
    <div class="name-band">Joan</div>
    <ul class="contact">
      <li class="contact__phone">509 314 6620</li>
      <li class="contact__web">www.vessasalon-example.com</li>
      <li class="contact__social">
        <svg width="14" height="14" viewBox="0 0 14 14" aria-hidden="true">
          <rect width="14" height="14" fill="var(--ink-white)"/>
        </svg>
        <span>/vessasalon</span>
      </li>
    </ul>
  </section>
</main>
</body>
</html>
```